Fabric Softener

We need fabric softener. Bottle picture attached for reference. Color of bottle can be proposed as well. Normally bottle is pink and blue color

Logo is also attached that shall be used.

Target Market(s)

Niche

Font styles to use
Sans Serif

Requirements
Must have
• Fabric, Brightness, Nature
Nice to have
• Good colors
Should not have
• Adults

```html
<!DOCTYPE html>
<html lang="en">
<head>
<meta charset="utf-8">
<title>Lumelle Fabric Softener – Label</title>
<link href="https://fonts.googleapis.com/css2?family=Cinzel:wght@500;600&family=Cormorant+Garamond:wght@500;700&family=Montserrat:wght@500;700&display=swap" rel="stylesheet">
<style>
  :root{
    --backdrop:#5a2a72;
    --label-dark:#3b1e4e;
    --label-mid:#9a4a98;
    --label-deep:#4a1f80;
    --label-edge:#ffffff;
    --soft-blue:#dfe6f5;
    --gold:#ecdf8c;
    --sand:#f0d7a4;
    --brand-white:#ffffff;
    --badge-dark:#3a1a55;
    --badge-light:#7a3a8e;
    --art-glow:#7a46c8;
    --art-warm:#b0386e;
  }
  html,body{margin:0;padding:0;overflow:hidden;}
  body{width:1200px;height:1200px;background:var(--backdrop);}
  .label{display:block;width:1200px;height:1200px;}
  .tagline-small{font-family:"Cormorant Garamond",serif;font-weight:500;font-size:66px;fill:var(--soft-blue);}
  .tagline-large{font-family:"Cormorant Garamond",serif;font-weight:500;font-size:96px;fill:var(--soft-blue);letter-spacing:2px;}
  .brand-name{font-family:"Cormorant Garamond",serif;font-weight:700;font-size:128px;fill:var(--brand-white);}
  .product-type-small{font-family:"Cinzel",serif;font-weight:600;font-size:40px;fill:var(--gold);letter-spacing:2px;}
  .product-type-large{font-family:"Cinzel",serif;font-weight:600;font-size:58px;fill:var(--gold);}
  .scent{font-family:"Montserrat",sans-serif;font-weight:700;font-size:26px;fill:var(--sand);letter-spacing:5px;}
  .load-count{font-family:"Montserrat",sans-serif;font-weight:700;font-size:58px;fill:var(--gold);}
  .load-unit{font-family:"Montserrat",sans-serif;font-weight:500;font-size:14px;fill:var(--gold);letter-spacing:1px;}
  .volume{font-family:"Montserrat",sans-serif;font-weight:500;font-size:22px;fill:var(--brand-white);}
</style>
</head>
<body>
<svg class="label" viewBox="330 540 1220 1220" xmlns="http://www.w3.org/2000/svg">
  <defs>
    <linearGradient id="labelFill" x1="0" y1="0" x2="1" y2="0">
      <stop offset="0" stop-color="var(--label-dark)"/>
      <stop offset="0.5" stop-color="var(--label-mid)"/>
      <stop offset="1" stop-color="var(--label-deep)"/>
    </linearGradient>
    <radialGradient id="artFill" cx="0.55" cy="0.5" r="0.55">
      <stop offset="0" stop-color="var(--art-warm)" stop-opacity="0.55"/>
      <stop offset="0.5" stop-color="var(--art-glow)" stop-opacity="0.35"/>
      <stop offset="1" stop-color="var(--art-glow)" stop-opacity="0"/>
    </radialGradient>
    <radialGradient id="badgeFill" cx="0.4" cy="0.35" r="0.7">
      <stop offset="0" stop-color="var(--badge-light)"/>
      <stop offset="1" stop-color="var(--badge-dark)"/>
    </radialGradient>
    <clipPath id="labelClip">
      <path d="M500 1150 C520 850 700 600 940 585 Q975 585 978 625 L1020 1220 C1030 1340 1100 1400 1200 1400 L1310 1400 Q1365 1400 1365 1460 L1365 1660 Q1365 1720 1305 1720 L560 1720 Q500 1720 500 1660 Z"/>
    </clipPath>
  </defs>

  <path class="label-body" d="M500 1150 C520 850 700 600 940 585 Q975 585 978 625 L1020 1220 C1030 1340 1100 1400 1200 1400 L1310 1400 Q1365 1400 1365 1460 L1365 1660 Q1365 1720 1305 1720 L560 1720 Q500 1720 500 1660 Z" fill="url(#labelFill)" stroke="var(--label-edge)" stroke-width="8"/>

  <g clip-path="url(#labelClip)">
    <rect class="hero-art" role="img" aria-label="Illustration of flowing soft fabric with starry sparkles" x="500" y="760" width="520" height="460" fill="url(#artFill)"/>
  </g>

  <text class="tagline-small" x="772" y="712">Ultra</text>
  <text class="tagline-large" x="700" y="792">SOFT</text>

  <g class="brand">
    <text class="brand-name" x="770" y="1310" text-anchor="middle">Lumelle</text>
  </g>

  <g class="load-badge">
    <circle cx="722" cy="1455" r="50" fill="url(#badgeFill)"/>
    <text class="load-count" x="722" y="1470" text-anchor="middle">48</text>
    <text class="load-unit" x="734" y="1492" text-anchor="middle">LOADS</text>
  </g>

  <text class="product-type-small" x="808" y="1410">FABRIC</text>
  <text class="product-type-large" x="806" y="1462">SOFTENER</text>
  <text class="scent" x="1100" y="1492" text-anchor="end">HEAVENLY</text>
  <text class="scent" x="1100" y="1524" text-anchor="end">BLOSSOM</text>

  <text class="volume" x="955" y="1675" text-anchor="middle">1.23 L (1.29 US QT) 41 FL OZ LIQ.</text>
</svg>
</body>
</html>
```